VantoreQuell Business Card Re-Design

VantoreQuell is a specialized information security company that applies its proven methodology of security Assessment, Development, Integration and Training (A-D-I-T) to provide cyber security services in the areas of Data Protection, Network Defense and Compliance. We need the current business card re-designed to properly scale the fonts and possibly rearranging some elements (icons, lettering, etc.) to make the card more appealing to the eye. The card should have the logo that is on the web site (www.vantorequell.example). We would like ideas for both a black card (black background) and a white card (white background). We prefer rounded corners to help the card stand out but are open to all ideas. FYI: VantoreQuell's slogan is "...your security is our business".

Target Market(s)

#1 US Government Contracting Companies, #2 Commercial Companies, #3 Gen. Public.

Industry/Entity Type

Business

Contact Information for Business Card

See Description; open to the use of different fonts.

Font styles to use
Sans Serif

Colors
000000
ec1f27
ffffff

Requirements
Must have
• Company logo on web site, rounded corners, list of company offerings on the back of the card.
Nice to have
• Icons
Should not have
• none

```html
<!DOCTYPE html>
<html lang="en">
<head>
<meta charset="utf-8">
<title>VantoreQuell Business Card</title>
<link rel="stylesheet" href="https://fonts.googleapis.com/css2?family=Roboto:wght@300;400;500;700&display=swap">
<style>
  :root {
    --black: #000000;
    --red: #ec1f27;
    --white: #ffffff;
    --panel: #2a2a2a;
    --panel-edge: #3a3a3a;
    --stage: #1c1c1e;
    --muted: #cfcfcf;
  }
  * { box-sizing: border-box; margin: 0; padding: 0; }
  html, body { width: 1200px; height: 873px; overflow: hidden; }
  body {
    background: var(--stage);
    font-family: "Roboto", Arial, sans-serif;
    color: var(--white);
    position: relative;
  }
  .card {
    position: absolute;
    top: 282px;
    width: 540px;
    height: 309px;
    background: var(--black);
    border-radius: 16px;
    overflow: hidden;
    box-shadow: 0 10px 30px rgba(0,0,0,.5);
  }
  .card--front { left: 40px; }
  .card--back { left: 620px; }

  /* Wordmark */
  .wordmark { display: flex; align-items: center; gap: 12px; }
  .wordmark__square { width: 18px; height: 18px; background: var(--red); }
  .wordmark__name {
    font-size: 26px; font-weight: 300; letter-spacing: 3px; color: var(--white);
  }
  .tagline { font-size: 11px; font-weight: 300; color: var(--muted); letter-spacing: .5px; margin-top: 6px; }

  /* Front */
  .front__brand { position: absolute; left: 34px; top: 48px; }
  .contact {
    position: absolute; left: 250px; top: 104px; right: 0; bottom: 42px;
    background: var(--panel); border-left: 10px solid var(--panel-edge);
  }
  .contact__band {
    background: var(--red); padding: 8px 18px 7px;
  }
  .contact__name { font-size: 20px; font-weight: 500; }
  .contact__creds { font-size: 10px; font-weight: 400; margin-left: 6px; }
  .contact__role { font-size: 10px; font-weight: 300; margin-top: 1px; }
  .contact__list { list-style: none; padding: 10px 18px; }
  .contact__list li {
    display: flex; align-items: center; gap: 10px;
    font-size: 11px; font-weight: 300; line-height: 19px;
  }
  .icon { width: 12px; height: 12px; flex: none; }
  .strip {
    position: absolute; left: 0; right: 0; bottom: 0; height: 42px;
    background: var(--red);
    display: flex; align-items: center; padding-left: 22px; gap: 10px;
    font-size: 11px; font-weight: 300;
  }

  /* Back */
  .back__brand {
    position: absolute; top: 40px; left: 0; right: 0;
    display: flex; flex-direction: column; align-items: center;
  }
  .services {
    position: absolute; top: 110px; width: 235px; list-style: none;
    font-size: 9.5px; font-weight: 400; line-height: 15px; color: var(--white);
  }
  .services--left { left: 26px; }
  .services--right { right: 20px; }
  .slogan {
    position: absolute; left: 0; right: 0; bottom: 0; height: 42px;
    background: var(--red);
    display: flex; align-items: center; justify-content: center;
    font-size: 15px; font-weight: 500; letter-spacing: .3px;
  }
</style>
</head>
<body>

<section class="card card--front" aria-label="Business card front">
  <div class="front__brand">
    <div class="wordmark">
      <span class="wordmark__square"></span>
      <span class="wordmark__name">VantoreQuell</span>
    </div>
    <p class="tagline">Information Security Solutions</p>
  </div>

  <div class="contact">
    <div class="contact__band">
      <p><span class="contact__name">Darren Holt</span><span class="contact__creds">CISSP, CEH</span></p>
      <p class="contact__role">President - CEO</p>
    </div>
    <ul class="contact__list">
      <li>
        <svg class="icon" viewBox="0 0 12 12"><path fill="var(--red)" d="M2 1h3l1 3-2 1a7 7 0 0 0 3 3l1-2 3 1v3c-6 0-10-4-10-10z"/></svg>
        555.210.4836
      </li>
      <li>
        <svg class="icon" viewBox="0 0 12 12"><rect x="3" y="0.5" width="6" height="11" rx="1" fill="var(--red)"/><rect x="4" y="2" width="4" height="7" fill="var(--panel)"/></svg>
        555.318.7742
      </li>
      <li>
        <svg class="icon" viewBox="0 0 12 12"><circle cx="6" cy="6" r="5" fill="none" stroke="var(--red)" stroke-width="1.2"/><ellipse cx="6" cy="6" rx="2.2" ry="5" fill="none" stroke="var(--red)"/><path d="M1 6h10" stroke="var(--red)"/></svg>
        www.vantorequell.example
      </li>
      <li>
        <svg class="icon" viewBox="0 0 12 12"><rect x="0.5" y="2" width="11" height="8" fill="var(--red)"/><path d="M0.5 2l5.5 4.5L11.5 2" fill="none" stroke="var(--panel)"/></svg>
        info@vantorequell.example
      </li>
      <li>
        <svg class="icon" viewBox="0 0 12 12"><rect x="0.5" y="2" width="11" height="8" fill="var(--red)"/><path d="M0.5 2l5.5 4.5L11.5 2" fill="none" stroke="var(--panel)"/></svg>
        dholt@vantorequell.example
      </li>
    </ul>
  </div>

  <div class="strip">
    <svg class="icon" viewBox="0 0 12 12"><path fill="none" stroke="var(--white)" stroke-width="1.2" d="M6 11.5S2 7 2 4.5a4 4 0 0 1 8 0C10 7 6 11.5 6 11.5z"/><circle cx="6" cy="4.5" r="1.3" fill="var(--white)"/></svg>
    <span>VantoreQuell, Inc. // 1420 Harlow Ave. Suite 12 // Linden Falls, Ohio 44512</span>
  </div>
</section>

<section class="card card--back" aria-label="Business card back">
  <div class="back__brand">
    <div class="wordmark">
      <span class="wordmark__square"></span>
      <span class="wordmark__name">VantoreQuell</span>
    </div>
  </div>

  <ul class="services services--left">
    <li>Secure Cloud &amp; Open Stack Solutions</li>
    <li>Network Attack Penetration &amp; Defense</li>
    <li>Red/Blue Team</li>
    <li>Data Center Consolidation</li>
    <li>Secure Virtual Computing</li>
    <li>Classified Cross Domain Solutions</li>
    <li>Foreign/Counterintelligence Data Security</li>
  </ul>

  <ul class="services services--right">
    <li>Certification and Accreditation</li>
    <li>Secure Wireless Solutions</li>
    <li>Security Training, Assessment &amp; Integration</li>
    <li>Security Subject Matter Experts</li>
    <li>Executive Security Strategy Coaching</li>
    <li>Data Encryption/Privacy</li>
  </ul>

  <p class="slogan">“Your security is our business.”</p>
</section>

</body>
</html>
```